Big carpet cleaning van wrap

Looking for a vehicle wrap for our second varn cadello van.
I will attach our current van pictures. And current logo too.
We will need something similar, not necessarily the same.

Target Market(s)

Homeowners, residential and commercial.

Industry/Entity Type

Carpet, tile and upholstery cleaning.

Other font styles liked:
• up to designer

Colors
0054AA
0677BA
7BADD7
CADEEF
E8F1F8
00AB8E
00BBA5
67D7C9
C6EFE9
E9F9F6

Requirements
Must have
• clear message.
Nice to have
• we would like to see similar colors, logo could be rebranded a bit and font as well.

```html
<!DOCTYPE html>
<html lang="en">
<head>
<meta charset="utf-8">
<title>BrightWave – Van Wrap Side Panel</title>
<link rel="stylesheet" href="https://fonts.googleapis.com/css2?family=Fjalla+One&family=Varela+Round&display=swap">
<style>
  :root {
    --page: #eef1f4;
    --wrap-white: #ffffff;
    --navy-blue: #1f4fa3;
    --deep-blue: #0054aa;
    --sky-blue: #36b3e0;
    --leaf-green: #4fae3a;
    --band-black: #141414;
    --text-white: #ffffff;
    --tag-navy: #1c3f8f;
  }
  html, body {
    margin: 0;
    padding: 0;
    width: 1200px;
    height: 555px;
    overflow: hidden;
    background: var(--page);
  }
  .wrap-canvas {
    display: block;
    width: 1200px;
    height: 555px;
  }
  .panel-base { fill: var(--wrap-white); }
  .band-sky { fill: var(--sky-blue); }
  .band-blue { fill: var(--navy-blue); }
  .band-green { fill: var(--leaf-green); }
  .band-black { fill: var(--band-black); }
  .web-address {
    font-family: "Fjalla One", sans-serif;
    font-size: 40px;
    fill: var(--text-white);
    letter-spacing: 1px;
  }
  .brand-name {
    font-family: "Varela Round", sans-serif;
    font-size: 116px;
    fill: var(--text-white);
  }
  .tagline-pill { fill: var(--wrap-white); }
  .tagline {
    font-family: "Varela Round", sans-serif;
    font-size: 27px;
    fill: var(--tag-navy);
  }
  .phone-number {
    font-family: "Fjalla One", sans-serif;
    font-size: 44px;
    fill: var(--text-white);
    letter-spacing: 12px;
  }
  .social-dot { fill: var(--text-white); }
  .phone-badge { fill: var(--text-white); }
  .phone-glyph { fill: var(--band-black); }
</style>
</head>
<body>
<svg class="wrap-canvas" viewBox="0 0 1200 555" xmlns="http://www.w3.org/2000/svg">
  <defs>
    <clipPath id="panel-clip">
      <rect x="40" y="60" width="1120" height="420" rx="18"/>
    </clipPath>
  </defs>

  <!-- wrap panel -->
  <rect class="panel-base" x="40" y="60" width="1120" height="420" rx="18"/>

  <g clip-path="url(#panel-clip)">
    <!-- colour bands -->
    <polygon class="band-sky" points="40,300 250,258 160,385 40,385"/>
    <polygon class="band-blue" points="150,385 200,285 460,185 905,60 1160,60 1160,255 830,330 340,372"/>
    <polygon class="band-green" points="830,330 1160,248 1160,285 850,330"/>
    <polygon class="band-black" points="330,372 1160,282 1160,362 345,440 330,420"/>
    <polygon class="band-blue" points="345,440 560,419 560,428 350,445"/>
    <polygon class="band-green" points="350,445 700,405 480,440"/>
  </g>

  <!-- social spots -->
  <circle class="social-dot" cx="222" cy="328" r="11"/>
  <circle class="social-dot" cx="255" cy="325" r="11"/>
  <circle class="social-dot" cx="288" cy="321" r="11"/>

  <!-- main message -->
  <g transform="rotate(-16 470 228)">
    <text class="web-address" x="470" y="228">www.brightwaveclean.com</text>
  </g>
  <g transform="rotate(-15 410 345)">
    <text class="brand-name" x="410" y="345">BrightWave</text>
  </g>
  <g transform="rotate(-15 680 330)">
    <rect class="tagline-pill" x="670" y="292" width="470" height="46" rx="23"/>
    <text class="tagline" x="690" y="324">carpet, tile and upholstery cleaning</text>
  </g>

  <!-- phone -->
  <circle class="phone-badge" cx="460" cy="386" r="15"/>
  <path class="phone-glyph" d="M453 379 q2 -3 4 -1 l2 3 q1 2 -1 3 q1 3 4 5 q1 -2 3 -1 l3 2 q2 2 -1 4 q-4 3 -10 -3 q-6 -6 -4 -12 z"/>
  <g transform="rotate(-5 520 402)">
    <text class="phone-number" x="520" y="402">555.014.2290</text>
  </g>
</svg>
</body>
</html>
```